on the groove website, music production company www.onthegroove.com

We are a music production company and need a new website to display some of our video clips which are mostly 30 seconds long. Below you can see some of our artwork (for example only, these are poor quality). I would need a home page to explain the company and then scroll downward to see thumbnails of the videos for viewing. Also, the ability to post audio files, for both listening, and perhaps for downloading with permission. Very simple. I usually like a retro style, ie the 60's. The character in our logo is known as "The Swingmiss" which is inspired by the English music scene in the 1960's. Thank you.
Updates

Here are some examples of my competitors: https://www.pourmehoney.com http://kelvorglobal.com https://www.tugtugtug.com/#thework http://www.throbsoundla.com I post these just so you can see how examples of the work are displayed. I don't need any fancy video at the top, only a way to present video clips to be viewed.

Simple like this would be great: http://www.throbsoundla.com I already posted a few sites, but this particular one is simple and would work perfectly.

Target Market(s)

We sell music for advertising, for tv commercials, so we are selling to creative people at advertising agencies.

Industry/Entity Type

Advertising

Number of Pages Required

2 page

Font styles to use
Sans Serif

Colors

Designer to choose colors to be used in the design.

Requirements
Must have
• The ability to post our video clips and our audio clips. The files I have are mostly .mov. I will have to send you our work, files are large.
• The official name of the company is on the groove productions, inc.
• It should also incorporate my name, Jan Mortell, and a bio on an "about us" page.
Nice to have
• The ability to easily add new videos to the site as the are available, ie, add new work in the future. If you need more information, please contact me to discuss further. Thank you. Jan

```html
<!DOCTYPE html>
<html lang="en">
<head>
<meta charset="utf-8">
<title>on the groove — original music and sound design</title>
<link href="https://fonts.googleapis.com/css2?family=Poppins:wght@400;500;600;700;800;900&family=Raleway:wght@400;500;600&display=swap" rel="stylesheet">
<style>
:root{
  --orange:#f26a1b;
  --orange-dark:#c9480a;
  --cream:#f8e3a8;
  --cream-back:#f6d98b;
  --ink:#1c1c1c;
  --dark:#1e1e1e;
  --darker:#161616;
  --gray-bg:#ececee;
  --text:#3a3a3a;
  --white:#ffffff;
}
*{margin:0;padding:0;box-sizing:border-box}
html,body{width:1200px;height:3719px;overflow:hidden}
body{position:relative;background:var(--white);font-family:"Raleway",sans-serif;color:var(--text)}
.abs{position:absolute}

/* hero */
.hero{left:0;top:0;width:1200px;height:739px;background:radial-gradient(ellipse at 50% 60%,#5a4534 0%,#2f241c 45%,#141010 100%)}
.brand{left:144px;top:55px;width:307px;height:69px}
.brand-name{font-family:"Poppins",sans-serif;font-weight:800;font-size:44px;line-height:46px;color:var(--orange);letter-spacing:1px}
.brand-tag{font-family:"Poppins",sans-serif;font-weight:500;font-size:12px;letter-spacing:2px;color:#f3d9a6;margin-top:2px}
.account{top:50px;height:34px;border:2px solid #fff;border-radius:18px;color:#fff;font-family:"Poppins",sans-serif;font-size:14px;font-weight:500;display:flex;align-items:center;justify-content:center;gap:6px}
.nav{top:106px;left:514px;display:flex;gap:0;font-family:"Poppins",sans-serif;font-weight:600;font-size:16px;color:#fff}
.nav span{position:absolute;white-space:nowrap}
.hero-title{left:0;width:1200px;top:305px;text-align:center;font-family:"Poppins",sans-serif;font-weight:700;font-size:74px;color:#fff;letter-spacing:1px}
.hero-sub{left:0;width:1200px;top:390px;text-align:center;font-family:"Poppins",sans-serif;font-weight:600;font-size:30px;color:#fff}
.btn-ghost{left:513px;top:462px;width:172px;height:38px;border:2px solid #fff;border-radius:20px;color:#fff;font-family:"Poppins",sans-serif;font-weight:600;font-size:15px;display:flex;align-items:center;justify-content:center}
.arrow{top:375px;color:#fff;font-size:26px;font-family:"Poppins",sans-serif}

/* about */
.card-back{background:var(--cream-back)}
.card{background:var(--cream);border:7px solid var(--orange)}
.about-photo{left:198px;top:731px;width:238px;height:238px;border-radius:50%;background:radial-gradient(circle at 45% 40%,#c98a5e,#6b4a3c 60%,#3a2a24);border:6px solid #1c1c1c}
.section-title{font-family:"Poppins",sans-serif;font-weight:900;color:var(--orange);text-shadow:-2px -2px 0 #5a2a08,2px -2px 0 #5a2a08,-2px 2px 0 #5a2a08,2px 2px 0 #5a2a08;letter-spacing:.5px}
.about-title{left:488px;top:718px;font-size:38px}
.about-text{left:488px;top:786px;width:510px;font-size:15.5px;line-height:27px;color:#444}
.btn-outline{left:488px;top:959px;width:118px;height:34px;border:2px solid var(--ink);border-radius:18px;font-family:"Poppins",sans-serif;font-weight:600;font-size:12.5px;color:var(--ink);display:flex;align-items:center;justify-content:center}

/* work */
.work-title{left:0;width:1200px;top:1145px;text-align:center;font-size:40px}
.work-grid{left:0;top:1247px;width:1200px;height:766px;display:grid;grid-template-columns:repeat(3,1fr);grid-template-rows:repeat(4,1fr);gap:2px;background:#fff}
.tile{position:relative}
.tile-feature{display:flex;flex-direction:column;align-items:center;justify-content:center;color:#fff;font-family:"Poppins",sans-serif}
.tile-feature b{font-size:17px;font-weight:600;letter-spacing:1px}
.tile-feature i{font-style:normal;font-size:13px;margin-top:6px}

/* audio */
.audio-bg{left:0;top:2013px;width:1200px;height:1098px;background:linear-gradient(180deg,#f4f4f5 0%,var(--gray-bg) 100%)}
.audio-title{left:0;width:1200px;top:2085px;text-align:center;font-size:40px}
.track{width:441px;height:156px;background:#fff;box-shadow:0 2px 10px rgba(0,0,0,.15)}
.track-thumb{position:absolute;left:20px;top:16px;width:114px;height:129px}
.track-title{position:absolute;left:160px;top:14px;font-family:"Poppins",sans-serif;font-weight:500;font-size:20px;color:#222}
.track-text{position:absolute;left:160px;top:52px;width:265px;font-size:12px;line-height:18px;color:#444}
.player{position:absolute;left:160px;top:120px;width:268px;height:20px}

/* testimonials */
.footer-band{left:0;top:3111px;width:1200px;height:526px;background:var(--dark)}
.testi-title{left:144px;width:910px;top:2912px;text-align:center;font-size:38px}
.quote{top:2968px;font-family:"Poppins",sans-serif;font-size:60px;color:#c9b07a;line-height:1}
.stars{left:540px;top:2982px;width:120px}
.testi-text{left:210px;width:780px;top:3034px;text-align:center;font-size:15.5px;line-height:29px;color:#444}
.testi-name{left:144px;width:910px;top:3168px;text-align:center;font-size:16px;color:#333}
.testi-name small{font-size:12px}

/* footer */
.foot-h{top:3345px;font-family:"Poppins",sans-serif;font-weight:600;font-size:17px;color:#fff}
.foot-t{font-size:13px;line-height:19px;color:#ddd}
.input{left:439px;top:3456px;width:273px;height:34px;border-radius:18px;background:#fff;font-size:11px;color:#888;padding:10px 18px}
.btn-sub{left:439px;top:3505px;width:101px;height:34px;border-radius:18px;background:var(--orange);color:#fff;font-family:"Poppins",sans-serif;font-weight:600;font-size:11px;display:flex;align-items:center;justify-content:center}
.links{left:778px;top:3398px;font-size:13px;line-height:24.5px;color:#ddd}
.social{left:964px;top:3400px;font-size:13px;color:#ddd}
.social div{display:flex;align-items:center;gap:10px;height:34px}
.social span.dot{width:22px;height:22px;border:1.5px solid #ddd;border-radius:50%}
.copy-bar{left:0;top:3637px;width:1200px;height:82px;background:var(--darker);border-top:1px solid #333;display:flex;align-items:center;justify-content:center;color:#ddd;font-size:14px}
</style>
</head>
<body>

<!-- hero -->
<div class="abs hero" role="img" aria-label="Overhead view of a producer at a studio mixing desk"></div>
<div class="abs brand">
  <div class="brand-name">on the groove</div>
  <div class="brand-tag">original music and sound design</div>
</div>
<div class="abs account" style="left:806px;width:127px">
  <svg width="12" height="12" viewBox="0 0 12 12"><circle cx="6" cy="3.5" r="3" fill="#fff"/><path d="M0 12c0-4 3-5.5 6-5.5S12 8 12 12z" fill="#fff"/></svg>REGISTER</div>
<div class="abs account" style="left:947px;width:107px">
  <svg width="11" height="13" viewBox="0 0 11 13"><rect x="0" y="5.5" width="11" height="7.5" rx="1" fill="#fff"/><path d="M2.5 5.5V4a3 3 0 0 1 6 0v1.5" stroke="#fff" stroke-width="1.6" fill="none"/></svg>LOG IN</div>
<nav class="abs nav">
  <span style="left:0">HOME</span>
  <span style="left:85px">ABOUT</span>
  <span style="left:180px">MUSIC PRODUCTION</span>
  <span style="left:361px">BLOG</span>
  <span style="left:438px">CONTACT US</span>
</nav>
<div class="abs arrow" style="left:106px">&#8249;</div>
<div class="abs arrow" style="left:1073px">&#8250;</div>
<h1 class="abs hero-title">ON THE GROOVE</h1>
<div class="abs hero-sub">ORIGINAL MUSIC AND SOUND DESIGN</div>
<div class="abs btn-ghost">GET MORE INFO</div>

<!-- about -->
<div class="abs card-back" style="left:150px;top:660px;width:880px;height:400px;transform:rotate(-5deg)"></div>
<div class="abs card" style="left:144px;top:682px;width:910px;height:355px"></div>
<div class="abs about-photo" role="img" aria-label="Portrait photo of Jan Mortell"></div>
<h2 class="abs section-title about-title">ABOUT JAN MORTELL</h2>
<p class="abs about-text">Sed ut perspiciatis unde omnis iste natus error sit voluptatem accusantium doloremque laudantium, totam rem aperiam, eaque ipsa quae ab illo inventore veritatis et quasi architecto beatae vitae dicta sunt explicabo. Nemo enim ipsam voluptatem quia voluptas sit aspernatur aut odit aut fugit, sed quia consequuntur magni dolores eos qui ratione voluptatem sequi nesciunt.</p>
<div class="abs btn-outline">READ MORE</div>

<!-- work -->
<h2 class="abs section-title work-title">THE WORK</h2>
<div class="abs work-grid">
  <div class="tile" role="img" aria-label="Video clip: couple with guitar" style="background:linear-gradient(135deg,#9aa8b0,#5f5e58)"></div>
  <div class="tile tile-feature" role="img" aria-label="Video clip: live concert crowd" style="background:linear-gradient(135deg,#d9772c,#b5541a)"><b>CLASS APTENT TACITI</b><i>&#9679; VIEW</i></div>
  <div class="tile" role="img" aria-label="Video clip: singer at microphone" style="background:linear-gradient(135deg,#3a3a3c,#6b5a4c)"></div>
  <div class="tile" role="img" aria-label="Video clip: guitarist and singer" style="background:linear-gradient(135deg,#4b4f55,#8a6f5c)"></div>
  <div class="tile" role="img" aria-label="Video clip: neon party glasses" style="background:linear-gradient(135deg,#7a2ea0,#d33a8a 55%,#f0a030)"></div>
  <div class="tile" role="img" aria-label="Video clip: singer on stage with camera crew" style="background:linear-gradient(135deg,#b7b9bd,#6d6560)"></div>
  <div class="tile" role="img" aria-label="Video clip: painted face fashion portrait" style="background:linear-gradient(135deg,#d9d6d2,#b45a36)"></div>
  <div class="tile" role="img" aria-label="Video clip: performer with microphone" style="background:linear-gradient(135deg,#dcdcdc,#5d5a58)"></div>
  <div class="tile" role="img" aria-label="Video clip: rock band on stage" style="background:linear-gradient(135deg,#6c7a86,#34383e)"></div>
  <div class="tile" role="img" aria-label="Video clip: dancers outdoors" style="background:linear-gradient(135deg,#e4dccf,#9b7a5f)"></div>
  <div class="tile" role="img" aria-label="Video clip: friends dancing in a street" style="background:linear-gradient(135deg,#cfc9b0,#c15f8a)"></div>
  <div class="tile" role="img" aria-label="Video clip: man with headphones in studio" style="background:linear-gradient(135deg,#7fa3c4,#3b3f4a)"></div>
</div>

<!-- audio -->
<div class="abs audio-bg"></div>
<h2 class="abs section-title audio-title">AUDIO</h2>

<svg width="0" height="0" style="position:absolute">
  <defs>
    <g id="player-ui">
      <circle cx="8" cy="10" r="7.5" fill="#555"/><path d="M6 6.5l5 3.5-5 3.5z" fill="#fff"/>
      <rect x="25" y="9" width="180" height="2.5" rx="1" fill="#555"/>
      <path d="M218 7h3l4-3.5v13l-4-3.5h-3z" fill="#555"/><path d="M228 6.5q3 3.5 0 7" stroke="#555" stroke-width="1.4" fill="none"/>
      <path d="M252 3v10M247.5 9l4.5 4.5 4.5-4.5M246 17h12" stroke="#555" stroke-width="2" fill="none"/>
    </g>
  </defs>
</svg>

<div class="abs track" style="left:144px;top:2196px"><div class="track-thumb" role="img" aria-label="Photographer with camera" style="background:linear-gradient(135deg,#4c4a48,#8e7a62)"></div><div class="track-title">Quis autem vel eum</div><p class="track-text">Sed ut perspiciatis unde omnis iste natus sit voluptatem accusantium doloremque laudantium, totam rem aperiam</p><svg class="player" viewBox="0 0 268 20"><use href="#player-ui"/></svg></div>
<div class="abs track" style="left:612px;top:2196px"><div class="track-thumb" role="img" aria-label="Cellist playing" style="background:linear-gradient(135deg,#2c2c30,#7b5a3e)"></div><div class="track-title">Quis autem vel eum</div><p class="track-text">Sed ut perspiciatis unde omnis iste natus sit voluptatem accusantium doloremque laudantium, totam rem aperiam</p><svg class="player" viewBox="0 0 268 20"><use href="#player-ui"/></svg></div>
<div class="abs track" style="left:144px;top:2380px"><div class="track-thumb" role="img" aria-label="Guitarist in green light" style="background:linear-gradient(135deg,#556b3a,#2f3024)"></div><div class="track-title">Quis autem vel eum</div><p class="track-text">Sed ut perspiciatis unde omnis iste natus sit voluptatem accusantium doloremque laudantium, totam rem aperiam</p><svg class="player" viewBox="0 0 268 20"><use href="#player-ui"/></svg></div>
<div class="abs track" style="left:612px;top:2380px"><div class="track-thumb" role="img" aria-label="Studio mixing screen" style="background:linear-gradient(135deg,#3c4e5e,#1e2a30)"></div><div class="track-title">Quis autem vel eum</div><p class="track-text">Sed ut perspiciatis unde omnis iste natus sit voluptatem accusantium doloremque laudantium, totam rem aperiam</p><svg class="player" viewBox="0 0 268 20"><use href="#player-ui"/></svg></div>
<div class="abs track" style="left:144px;top:2563px"><div class="track-thumb" role="img" aria-label="Acoustic guitar player" style="background:linear-gradient(135deg,#7a2e4e,#c0583a)"></div><div class="track-title">Quis autem vel eum</div><p class="track-text">Sed ut perspiciatis unde omnis iste natus sit voluptatem accusantium doloremque laudantium, totam rem aperiam</p><svg class="player" viewBox="0 0 268 20"><use href="#player-ui"/></svg></div>
<div class="abs track" style="left:612px;top:2563px"><div class="track-thumb" role="img" aria-label="Concert crowd with raised hands" style="background:linear-gradient(180deg,#3f6fb0,#121a2a)"></div><div class="track-title">Quis autem vel eum</div><p class="track-text">Sed ut perspiciatis unde omnis iste natus sit voluptatem accusantium doloremque laudantium, totam rem aperiam</p><svg class="player" viewBox="0 0 268 20"><use href="#player-ui"/></svg></div>

<!-- testimonials -->
<div class="abs footer-band"></div>
<div class="abs card-back" style="left:160px;top:2860px;width:900px;height:380px;transform:rotate(4deg)"></div>
<div class="abs card" style="left:144px;top:2876px;width:910px;height:355px"></div>
<h2 class="abs section-title testi-title">TESTIMONIALS</h2>
<div class="abs quote" style="left:492px">&ldquo;</div>
<div class="abs quote" style="left:672px">&rdquo;</div>
<svg class="abs stars" viewBox="0 0 120 18">
  <g fill="none" stroke="var(--orange)" stroke-width="1.4">
    <path id="star" d="M9 1.5l2.2 4.6 5 .7-3.6 3.5.9 5-4.5-2.4-4.5 2.4.9-5L1.8 6.8l5-.7z"/>
    <use href="#star" x="22"/><use href="#star" x="44"/><use href="#star" x="66"/><use href="#star" x="88"/>
  </g>
</svg>
<p class="abs testi-text">Sed ut perspiciatis unde omnis iste natus error sit voluptatem accusantium doloremque laudantium, totam rem aperiam, eaque ipsa quae ab illo inventore veritatis et quasi architecto beatae vitae dicta sunt explicabo. Nemo enim ipsam voluptatem quia voluptas sit aspernatur aut odit aut fugit Sed ut perspiciatis unde omnis iste natus error sit voluptatem</p>
<div class="abs testi-name">Blandit Lectus – <small>Groove productions, Inc</small></div>

<!-- footer -->
<div class="abs foot-h" style="left:144px">CONTACT US</div>
<svg class="abs" style="left:146px;top:3403px" width="12" height="16" viewBox="0 0 12 16"><path d="M6 15S1 9 1 6a5 5 0 0 1 10 0c0 3-5 9-5 9z" fill="none" stroke="#ddd" stroke-width="1.4"/><circle cx="6" cy="6" r="1.8" fill="#ddd"/></svg>
<div class="abs foot-t" style="left:175px;top:3400px;width:200px">Groove productions, Inc<br>48, 0 456 Lane Unit #2<br>Location.</div>
<svg class="abs" style="left:146px;top:3469px" width="14" height="14" viewBox="0 0 14 14"><path d="M3 1l2.5 3-1.5 1.5q1.5 3 4.5 4.5L10 8.5l3 2.5-1.5 2Q6 13 1 3z" fill="#ddd"/></svg>
<div class="abs foot-t" style="left:175px;top:3467px">Phone : +888 555 0147</div>
<svg class="abs" style="left:145px;top:3500px" width="16" height="12" viewBox="0 0 16 12"><rect x=".7" y=".7" width="14.6" height="10.6" fill="none" stroke="#ddd" stroke-width="1.3"/><path d="M1 1l7 6 7-6" fill="none" stroke="#ddd" stroke-width="1.3"/></svg>
<div class="abs foot-t" style="left:175px;top:3497px">Email : info@onthegroove.com</div>

<div class="abs foot-h" style="left:439px">SIGN UP TO RECEIVE EMAIL</div>
<div class="abs foot-t" style="left:439px;top:3400px;width:280px;font-size:11px;line-height:17px">Excepteur sint occaecat cupidatat non proident, sunt in culpa qui Nemo enim ipsam voluptatem</div>
<div class="abs input">Enter Email</div>
<div class="abs btn-sub">SUBSCRIBE</div>

<div class="abs foot-h" style="left:778px">QUICK LINKS</div>
<div class="abs links">Home<br>About Us<br>Music production<br>Blog<br>Contact Us</div>

<div class="abs foot-h" style="left:964px">SOCIAL</div>
<div class="abs social">
  <div><span class="dot"></span>Friendnet</div>
  <div><span class="dot"></span>Chirper</div>
  <div><span class="dot"></span>Searchly+</div>
  <div><span class="dot"></span>clipstream</div>
</div>

<div class="abs copy-bar">Copyright © Groove productions, inc. 2018. All rights reserved.</div>

</body>
</html>
```